Lakemont Hydro Partners, Inc. Company Brochure

I would like someone to design a brochure that can be handed out to prospective clients. We are a full service water and wastewater operations company that provides services to Municipal Utility Districts and citys. I would like something that is catchy to the eye and reflects a company that prides itself on providing personal service to its clients. We need to revamp our website, that's next, but the website does have a description of our company and services offered. You can find that information at www.lakemonthydropartners.example

```html
<!DOCTYPE html>
<html lang="en">
<head>
<meta charset="utf-8">
<title>Lakemont Hydro Partners, Inc. — Company Brochure</title>
<link rel="stylesheet" href="https://fonts.googleapis.com/css2?family=Source+Sans+3:wght@300;400;600;700&display=swap">
<style>
:root{
  --blue:#1f9ee0;
  --ink:#4a4f55;
  --grey:#6d7379;
  --paper:#ffffff;
  --stage:#e9eaeb;
  --teal-light:#8cc3ca;
  --teal-mid:#2f7986;
  --teal-deep:#0b3843;
}
*{box-sizing:border-box;margin:0;padding:0}
html,body{width:1200px;height:1163px;overflow:hidden}
body{background:var(--stage);font-family:"Source Sans 3",sans-serif;color:var(--ink);position:relative}
.page{position:absolute;background:var(--paper);overflow:hidden;box-shadow:0 1px 4px rgba(0,0,0,.12)}
.band{position:absolute;left:0;right:0;
  background:radial-gradient(ellipse 75% 70% at 50% 65%,var(--teal-light) 0%,var(--teal-mid) 45%,var(--teal-deep) 100%);
  color:#fff;text-align:center}
.tab{position:absolute;left:50%;width:34px;height:13px;margin-left:-17px;background:var(--paper)}
.tab.top{top:0;border-radius:0 0 17px 17px}
.tab.bottom{bottom:0;border-radius:17px 17px 0 0}
.brand{color:var(--blue);text-align:center;font-weight:600;text-transform:uppercase;letter-spacing:.08em;line-height:1.02}
.tagline{color:var(--grey);text-align:center}
.mark{position:absolute;left:50%;border:3px solid var(--blue);border-radius:50%;background:var(--paper)}
.heading{color:var(--blue);text-align:center;font-weight:400;text-transform:uppercase}
.headline{text-transform:uppercase;line-height:.88;letter-spacing:-.01em}
.headline b{font-weight:700}
.headline span{font-weight:300}
.waves{display:block;margin:0 auto}
.url{position:absolute;left:0;right:0;text-align:center;color:var(--grey);font-weight:600}
.body-copy{text-align:justify;font-size:11.4px;line-height:1.08;color:var(--ink)}
.services{display:grid;grid-template-columns:1fr 1fr;column-gap:12px;row-gap:5px;list-style:none;font-size:9.6px;line-height:1.02;font-weight:600;color:var(--ink)}
.services li{position:relative;padding-left:16px;min-height:20px}
.services li::before{content:"";position:absolute;left:2px;top:2px;width:4px;height:8px;border:solid var(--blue);border-width:0 2px 2px 0;transform:rotate(45deg)}
.fold{position:absolute;top:0;bottom:0;left:340px;width:1px;background:rgba(0,0,0,.08)}
</style>
</head>
<body>

<!-- Outer spread -->
<section class="page spread-outer" style="left:76px;top:33px;width:681px;height:530px">
  <div class="fold"></div>

  <div class="panel mission-panel" style="position:absolute;left:0;top:0;width:340px;height:530px">
    <p class="brand" style="margin-top:27px;font-size:15px">Lakemont Hydro<br>Partners Inc.</p>
    <p class="tagline" style="font-size:10px;margin-top:4px">A Full Service Operations Company</p>
    <div style="width:34px;height:2px;background:var(--blue);margin:19px auto 0"></div>
    <h2 class="heading" style="font-size:22px;margin-top:8px">Our Mission</h2>
    <div class="band" role="img" aria-label="Photo of water droplets on teal glass" style="top:148px;height:332px">
      <div style="width:240px;margin:32px auto 0;font-size:11px;font-weight:600;line-height:1.42;text-transform:uppercase">
        <p>Lakemont Hydro Partners, Inc. is a leading competitor in the utility operations industry and has achieved this status by maintaining the quality of work and relationships that few companies can offer.</p>
        <p style="margin-top:14px">Whether you are a district that is currently operated by an outside contract company or a district entertaining the concept, Lakemont Hydro Partners, Inc would be delighted to present a detailed quote for operations and services. Please contact our office and a representative will discuss the services that are currently available in your area.</p>
      </div>
    </div>
    <p style="position:absolute;top:500px;left:0;right:0;text-align:center;font-size:9.5px;line-height:1.1;color:var(--grey)">
      Office: <b style="color:var(--blue);font-weight:600">281-555-0147</b> Toll Free <b style="color:var(--blue);font-weight:600">800-555-0193</b><br>
      4820 Cedar Ridge Rd #210 Lakemont, TX 77000
    </p>
  </div>

  <div class="panel cover-panel" style="position:absolute;left:341px;top:0;width:340px;height:530px">
    <p class="brand" style="margin-top:30px;font-size:23px">Lakemont Hydro<br>Partners Inc.</p>
    <p class="tagline" style="font-size:15px;margin-top:6px">A Full Service Operations Company</p>
    <div class="band" role="img" aria-label="Photo of water droplets on teal glass" style="top:147px;height:345px">
      <div class="tab top"></div>
      <div class="tab bottom"></div>
      <p class="headline" style="margin-top:92px;font-size:29px">
        <b>We have</b> <span>a fully</span><br><span>staffed billing and</span><br><b>collections office</b><br><span>to handle any of</span><br><b>your customers</b><br><b>needs</b>
      </p>
      <svg class="waves" width="36" height="20" viewBox="0 0 36 20" style="margin-top:12px" fill="none" stroke="#fff" stroke-width="2">
        <path d="M1 4q4.25-4 8.5 0t8.5 0 8.5 0 8.5 0"/><path d="M1 10q4.25-4 8.5 0t8.5 0 8.5 0 8.5 0"/><path d="M1 16q4.25-4 8.5 0t8.5 0 8.5 0 8.5 0"/>
      </svg>
    </div>
    <div class="mark" style="top:128px;width:32px;height:32px;margin-left:-16px"></div>
    <p class="url" style="top:503px;font-size:11px">www.lakemonthydropartners.example</p>
  </div>
</section>

<!-- Inner spread -->
<section class="page spread-inner" style="left:76px;top:594px;width:681px;height:530px">
  <div class="fold"></div>

  <div class="panel about-panel" style="position:absolute;left:0;top:0;width:340px;height:530px">
    <h2 class="heading" style="font-size:22px;margin-top:16px">About Us</h2>
    <div class="band" role="img" aria-label="Photo of water droplets on teal glass" style="top:51px;height:193px">
      <p style="margin-top:47px;font-size:21px;line-height:.98;text-transform:uppercase;font-weight:400">Lakemont Hydro<br>Partners, Inc.<br>was incorporated in<br>the state of Texas<br>in 1989.</p>
    </div>
    <div style="position:absolute;top:258px;left:19px;right:19px">
      <p class="body-copy">Lakemont Hydro Partners, Inc. is a water and waste water utility operations and billing company. All personnel employed by Lakemont Hydro Partners, Inc. are licensed by the SWQB in water &amp; waste water operations and obtain the proper training needed to successfully operate treatment plants to their maximum capability. We are certified to operate surface water, ground water, and waste water treatment facilities to their maximum capability.</p>
      <p class="body-copy" style="margin-top:12px">We have a fully staffed billing and collections office to handle any of your customers needs. The mission of Lakemont Hydro Partners, Inc. is to provide the consumer with the highest caliber of services available. Our goal is to achieve this service for the Districts with the most competitive cost around.</p>
      <p style="text-align:center;color:var(--blue);font-size:24px;line-height:1.05;margin-top:16px;text-transform:uppercase;font-weight:300">We are a <b style="font-weight:600">24/7</b><br>operations company!</p>
    </div>
  </div>

  <div class="panel services-panel" style="position:absolute;left:341px;top:0;width:340px;height:530px">
    <h2 class="heading" style="font-size:22px;margin-top:14px">Services</h2>
    <div class="band" role="img" aria-label="Photo of water droplets on teal glass" style="top:51px;height:193px">
      <p style="margin-top:27px;font-size:21px;line-height:.98;text-transform:uppercase;font-weight:300">Lakemont Hydro<br>Partners, Inc. is a<br>“<b style="font-weight:600">Full Service</b>” operations<br>company that handles all<br>aspects of operations in<br>the water/waste water<br>utility industry.</p>
    </div>
    <div style="position:absolute;top:257px;left:20px;right:18px">
      <p class="body-copy" style="text-align:left;font-size:11px;line-height:1">Here at Lakemont Hydro Partners, Inc., we feel that it is important to provide the highest caliber of services available to the Districts in which we operate. We offer the ability to tailor our services based on the current needs of the District</p>
      <p style="font-size:11px;font-weight:600;margin:6px 0 14px">Services currently available are:</p>
      <ul class="services">
        <li>Surface Water Plant Operations</li><li>Meter Reading</li>
        <li>Waste Water Plant Operations</li><li>Consulting/Management</li>
        <li>Ground Water Well Operations</li><li>Lab Work and Reporting to any and all regulating agencies</li>
        <li>Distribution and Collection System maintenance and repairs</li><li>Project Planning</li>
        <li>New Construction Water and Sewer Taps, and all inspections required</li><li>Assist in Annual Budget Planning</li>
        <li>Billing and Collections</li><li>Smoke Testing</li>
        <li></li><li>Park and Trail maintenance</li>
        <li></li><li>Detention pond maintenance</li>
      </ul>
    </div>
  </div>
</section>

<!-- Single cover card -->
<section class="page cover-card" style="left:768px;top:225px;width:375px;height:555px">
  <p class="brand" style="margin-top:35px;font-size:25px">Lakemont Hydro<br>Partners Inc.</p>
  <p class="tagline" style="font-size:16px;margin-top:8px">A Full Service Operations Company</p>
  <div class="band" role="img" aria-label="Photo of water droplets on teal glass" style="top:150px;height:355px">
    <div class="tab top"></div>
    <div class="tab bottom"></div>
    <p class="headline" style="margin-top:96px;font-size:31px">
      <b>We have</b> <span>a fully</span><br><span>staffed billing and</span><br><b>collections office</b><br><span>to handle any of</span><br><b>your customers</b><br><b>needs</b>
    </p>
    <svg class="waves" width="40" height="22" viewBox="0 0 36 20" style="margin-top:14px" fill="none" stroke="#fff" stroke-width="2">
      <path d="M1 4q4.25-4 8.5 0t8.5 0 8.5 0 8.5 0"/><path d="M1 10q4.25-4 8.5 0t8.5 0 8.5 0 8.5 0"/><path d="M1 16q4.25-4 8.5 0t8.5 0 8.5 0 8.5 0"/>
    </svg>
  </div>
  <div class="mark" style="top:137px;width:32px;height:32px;margin-left:-16px"></div>
  <p class="url" style="top:518px;font-size:12px">www.lakemonthydropartners.example</p>
</section>

</body>
</html>
```